Red Sea Boat trips in need of Business Card for Private Boat Tours

We need a Business card for a new business set-up in Egypt on the Red Sea for private snorkelling and boat excursions to one of the world's most beautiful reefs. We have wording logo already set-up which matches the boat but we need business cards to be bright and colourful with pictures of boat

Industry/Entity Type

Tourism

Contact Information for Business Card

Two Silver Herons (font provided) Boat Trips

```html
<!DOCTYPE html>
<html lang="en">
<head>
<meta charset="utf-8">
<title>Two Silver Herons – Business Card</title>
<link href="https://fonts.googleapis.com/css2?family=Poppins:wght@400;700&family=Yellowtail&display=swap" rel="stylesheet">
<style>
  :root {
    --backdrop: #9b9b9b;
    --ink: #0b0b0b;
    --ink-soft: #2b2b2b;
    --sea-pale-top: #b7dfe0;
    --sea-pale-mid: #cdeceb;
    --sea-pale-low: #a9d6d4;
    --sea-deep-top: #1c4756;
    --sea-deep-mid: #2f6a6c;
    --sea-bright-low: #72cfd2;
  }
  * { box-sizing: border-box; margin: 0; padding: 0; }
  html, body {
    width: 1093px;
    height: 1200px;
    overflow: hidden;
    background: var(--backdrop);
  }
  .card {
    position: absolute;
    left: 265px;
    width: 578px;
    height: 357px;
    border-radius: 24px;
    overflow: hidden;
  }
  .card--front { top: 226px; }
  .card--back { top: 622px; }
  .card__photo {
    position: absolute;
    inset: 0;
    width: 100%;
    height: 100%;
  }
  .card__content {
    position: absolute;
    inset: 0;
    text-align: center;
    color: var(--ink);
  }
  .brand-name {
    position: absolute;
    left: 0;
    right: 0;
    font-family: "Poppins", sans-serif;
    font-weight: 700;
    font-size: 40px;
    line-height: 1;
    color: var(--ink);
  }
  .card--front .brand-name { top: 62px; }
  .card--back .brand-name { top: 155px; }
  .person-name {
    position: absolute;
    left: 0; right: 0;
    top: 148px;
    font-family: "Yellowtail", cursive;
    font-size: 40px;
    line-height: 1;
  }
  .person-role {
    position: absolute;
    left: 0; right: 0;
    top: 192px;
    font-family: "Poppins", sans-serif;
    font-size: 20px;
    line-height: 1;
  }
  .divider {
    position: absolute;
    left: 251px;
    top: 224px;
    width: 75px;
    height: 2px;
    background: var(--ink);
  }
  .phone {
    position: absolute;
    left: 0; right: 0;
    top: 244px;
    font-family: "Poppins", sans-serif;
    font-weight: 700;
    font-size: 44px;
    line-height: 1;
  }
  .website {
    position: absolute;
    left: 0; right: 0;
    top: 294px;
    font-family: "Poppins", sans-serif;
    font-size: 24px;
    line-height: 1;
    color: var(--ink-soft);
  }
</style>
</head>
<body>
  <section class="card card--front">
    <svg class="card__photo" viewBox="0 0 578 357" preserveAspectRatio="none" role="img" aria-label="Underwater photo of a snorkeller diving over a sandy Red Sea reef with coral, softly washed out">
      <defs>
        <linearGradient id="frontSea" x1="0" y1="0" x2="1" y2="1">
          <stop offset="0" stop-color="var(--sea-pale-top)"/>
          <stop offset="0.55" stop-color="var(--sea-pale-mid)"/>
          <stop offset="1" stop-color="var(--sea-pale-low)"/>
        </linearGradient>
      </defs>
      <rect width="578" height="357" fill="url(#frontSea)"/>
    </svg>
    <div class="card__content">
      <p class="brand-name">Two Silver Herons</p>
      <p class="person-name">Adrian Cole</p>
      <p class="person-role">Managing Director</p>
      <span class="divider"></span>
      <p class="phone">044-210 987 654</p>
      <p class="website">www.silverheronstrips.com</p>
    </div>
  </section>

  <section class="card card--back">
    <svg class="card__photo" viewBox="0 0 578 357" preserveAspectRatio="none" role="img" aria-label="Underwater photo of a snorkeller with fins diving toward a coral reef and bright sandy sea floor">
      <defs>
        <linearGradient id="backSea" x1="0" y1="0" x2="0.6" y2="1">
          <stop offset="0" stop-color="var(--sea-deep-top)"/>
          <stop offset="0.5" stop-color="var(--sea-deep-mid)"/>
          <stop offset="1" stop-color="var(--sea-bright-low)"/>
        </linearGradient>
      </defs>
      <rect width="578" height="357" fill="url(#backSea)"/>
    </svg>
    <div class="card__content">
      <p class="brand-name">Two Silver Herons</p>
    </div>
  </section>
</body>
</html>
```